Need 3 posters for in-store display

Hi Marlene,

Hope you are well.
I need 3 posters for display in my restaurant.

Poster 1: To be print in A1 size vertical
Title: SLURPALICIOUS DEAL $19.50
Choose any Pho OR Noodle Salads
Choose Spring Rolls (5 rolls) OR Ricepaper Rolls (2 rolls)
Choose any Cans OR Water

What I like to see:
- These poster will be place near my counter so I want it to grab customer attention.
- You must use photos to show products
- Make it easy to understand and for customer to follow

Poster 2: To be print in A4 size vertical
Title: ADD TO YOUR ORDER
SpringRolls (Crab / vegetarian) $6 / 5 rolls
Extra Meat $2
Extra Noodles $1
Extra Vegs $1.5
Extra Tofu $2
Extra Crackling $3

Poster 3: To be print in A1 size vertical
Title: BROTH BONANZA BASH
Catering Menu Options:
- PHO (Beef, Chicken, Vegan) $12.50 per bowl
- NOODLE SALADS (Beef, Chicken, BBQ Pork, Vegan) $12.50 per bowl
- SpringRolls (Crab / vegetarian) $12.50 for 10 rolls
- Ricepaper Rolls (Prawn, Beef, Chicken, BBQ Pork, Tofu) $12.5 / 5 rolls
- Fried Rice (Prawn, Tofu) $50 per tray (serve 5-6)

Terms & Conditions for All Catering Orders:
1) Minimum orders $200 (Pick-Up from shop Only)
2) All orders must be paid upfront
3) Requires $300 bond for Soup Tank
4) Please give us 48hours notice

Industry/Entity Type

Restaurant

Requirements
Nice to have
• For the SLURPALICIOUS DEAL
• it would be nice to have an image of the battle of water to visually complete the meal deal
• please see attachment of the Kestrel Ridge Water

```html
<!DOCTYPE html>
<html lang="en">
<head>
<meta charset="utf-8">
<title>Add to Order – Poster</title>
<link href="https://fonts.googleapis.com/css2?family=Bebas+Neue&family=Nanum+Brush+Script&display=swap" rel="stylesheet">
<style>
  :root {
    --canvas: #ffffff;
    --poster-black: #000000;
    --ink-light: #f1ece8;
    --photo-dark: #2a2a2c;
    --photo-plate: #f4f2f0;
    --photo-roll: #c9853a;
    --photo-sauce: #e0442a;
  }
  * { margin: 0; padding: 0; box-sizing: border-box; }
  html, body {
    width: 1200px;
    height: 1000px;
    overflow: hidden;
    background: var(--canvas);
  }
  .poster {
    position: absolute;
    left: 281px;
    top: 47px;
    width: 640px;
    height: 904px;
    background: var(--poster-black);
    overflow: hidden;
  }
  .poster__photo {
    position: absolute;
    left: 0;
    top: 0;
    width: 640px;
    height: 450px;
  }
  .poster__title {
    position: absolute;
    left: 30px;
    top: 372px;
    font-family: "Nanum Brush Script", cursive;
    font-weight: 400;
    font-size: 150px;
    line-height: 112px;
    color: var(--ink-light);
    letter-spacing: 2px;
  }
  .poster__title span { display: block; }
  .poster__title .title-line--second { margin-left: -6px; }
  .addon-list {
    position: absolute;
    left: 39px;
    top: 636px;
    list-style: none;
    font-family: "Bebas Neue", sans-serif;
    font-size: 31px;
    line-height: 37.5px;
    letter-spacing: 1.2px;
    color: var(--ink-light);
  }
</style>
</head>
<body>
  <main class="poster">
    <svg class="poster__photo" viewBox="0 0 640 450" role="img" aria-label="Photo of crispy fried spring rolls stacked on a white plate with a bowl of sweet chili dipping sauce">
      <defs>
        <linearGradient id="backdropTone" x1="0" y1="0" x2="0" y2="1">
          <stop offset="0" stop-color="#3a3a3c"/>
          <stop offset="1" stop-color="var(--photo-dark)"/>
        </linearGradient>
        <radialGradient id="plateTone" cx="0.5" cy="0.45" r="0.7">
          <stop offset="0" stop-color="#d49a55"/>
          <stop offset="0.45" stop-color="#e9d6c2"/>
          <stop offset="1" stop-color="var(--photo-plate)"/>
        </radialGradient>
      </defs>
      <rect x="0" y="0" width="640" height="320" fill="url(#backdropTone)"/>
      <polygon points="0,60 640,0 640,325 420,438 0,300" fill="url(#plateTone)"/>
    </svg>

    <h1 class="poster__title">
      <span class="title-line--first">Add</span>
      <span class="title-line--second">to order</span>
    </h1>

    <ul class="addon-list">
      <li>Springrolls (Crab / Vegetarian) $6 / 5 Rolls</li>
      <li>Extra Meat $2</li>
      <li>Extra Noodles $1</li>
      <li>Extra Vegs $1.5</li>
      <li>Extra Tofu $2</li>
      <li>Extra Crackling $3</li>
    </ul>
  </main>
</body>
</html>
```